KL MOTORS BANNER/SIGN DESIGN

Design a banner sign for outdoor use for KL MOTORS - a premium pre owned vehicle sales center. The size must be 36 feet in width
and 3 feet in height.

Information required: logo (attached)
-PREMIUM PRE-OWEND VEHICLE SALES
- 517.264.3081

perhaps in smaller font: BUY-SELL-TRADE

prefer white background but could possibly do red matching the logo

```html
<!DOCTYPE html>
<html lang="en">
<head>
<meta charset="utf-8">
<title>KL Motors Banner</title>
<link rel="stylesheet" href="https://fonts.googleapis.com/css2?family=Michroma&family=Oswald:wght@700&family=Syncopate:wght@700&display=swap">
<style>
  :root {
    --brand-red: #d91f26;
    --ink: #1c1416;
    --ink-soft: #2f2a2b;
    --paper: #ffffff;
    --stage: #efefef;
    --car-light: #f6f6f6;
    --car-mid: #c9cbcd;
    --car-dark: #6a6b6d;
  }
  html, body {
    margin: 0;
    padding: 0;
    width: 1200px;
    height: 600px;
    overflow: hidden;
    background: var(--stage);
  }
  .banner {
    position: absolute;
    left: 40px;
    top: 231px;
    width: 1120px;
    height: 138px;
    display: block;
  }
  .banner-frame { fill: var(--paper); stroke: #d8d8d8; stroke-width: 2; }
  .brand-band, .contact-band, .tag-pill { fill: var(--brand-red); }
  .brand-pill { fill: var(--paper); }
  .brand-name { font-family: "Syncopate", sans-serif; font-weight: 700; fill: var(--ink); }
  .tag-text { font-family: "Michroma", sans-serif; fill: var(--paper); }
  .headline { font-family: "Syncopate", sans-serif; font-weight: 700; fill: var(--ink); }
  .subline { font-family: "Syncopate", sans-serif; font-weight: 700; fill: var(--ink-soft); }
  .phone-icon { fill: var(--paper); }
  .phone-icon-dial { fill: var(--brand-red); }
  .phone-number { font-family: "Oswald", sans-serif; font-weight: 700; fill: var(--paper); }
</style>
</head>
<body>
<svg class="banner" viewBox="0 0 2249 278" xmlns="http://www.w3.org/2000/svg" aria-label="KL Motors premium pre-owned vehicle sales banner">
  <defs>
    <linearGradient id="car-tone" x1="0" y1="0" x2="0" y2="1">
      <stop offset="0%" stop-color="var(--car-light)"/>
      <stop offset="65%" stop-color="var(--car-mid)"/>
      <stop offset="100%" stop-color="var(--car-dark)"/>
    </linearGradient>
  </defs>

  <rect class="banner-frame" x="1" y="1" width="2247" height="276"/>

  <g class="brand-block">
    <path class="brand-band" d="M31,35 H432 C455,58 470,92 470,139 C470,188 455,220 430,243 H31 Z"/>
    <rect class="brand-pill" x="60" y="77" width="400" height="123" rx="61.5"/>
    <text class="brand-name" x="260" y="154" font-size="40" text-anchor="middle" textLength="300" lengthAdjust="spacingAndGlyphs">KL MOTORS</text>
  </g>

  <g class="tag-block">
    <rect class="tag-pill" x="480" y="88" width="338" height="102" rx="51"/>
    <text class="tag-text" x="650" y="136" font-size="36" text-anchor="middle" textLength="232" lengthAdjust="spacingAndGlyphs">PREMIUM</text>
    <text class="tag-text" x="650" y="170" font-size="31" text-anchor="middle" textLength="268" lengthAdjust="spacingAndGlyphs">PRE-OWNED</text>
  </g>

  <g class="headline-block">
    <text class="headline" x="851" y="150" font-size="58" textLength="667" lengthAdjust="spacingAndGlyphs">VEHICLE SALES</text>
    <text class="subline" x="896" y="184" font-size="22" textLength="580" lengthAdjust="spacing">BUY-SELL-TRADE</text>
  </g>

  <g class="contact-block">
    <path class="contact-band" d="M1835,35 H2218 V243 H1820 C1795,200 1790,150 1800,110 C1810,75 1820,50 1835,35 Z"/>
    <path role="img" aria-label="Photo of a white convertible sports car" fill="url(#car-tone)"
          d="M1556,130 C1560,105 1600,95 1650,90 C1690,70 1740,66 1790,72 C1830,80 1860,100 1868,140 C1870,170 1860,195 1830,205 L1600,212 C1570,205 1552,170 1556,130 Z"/>
    <g class="phone-icon">
      <path d="M1996,92 C1996,70 2068,70 2068,92 L2056,96 C2054,88 2010,88 2008,96 Z"/>
      <path d="M2012,96 H2052 L2060,126 H2004 Z"/>
      <circle class="phone-icon-dial" cx="2032" cy="110" r="8"/>
    </g>
    <text class="phone-number" x="2034" y="193" font-size="62" text-anchor="middle" textLength="305" lengthAdjust="spacingAndGlyphs">517.264.3081</text>
  </g>
</svg>
</body>
</html>
```